design a beautiful, neat and professional looking 10 page templete for an online course

I designed an online course. It about the newborn adoption process. I need you to design the template for it. Just the first 10 pages is enough. I'm thinking a neutral palette with a pop of a minor color to keep it from being boring. The pop of color should not distract the reader. You can design how you want. If you want to add small details or hearts or a shape in background you can. Just dont overdo it. Sparingly is the key. You can make pages a different color. It just needs to look like a neutral color palette with a small pop of color.
Updates

Low design quality

Target Market(s)

people who are adopting a newborn in the USA

Industry/Entity Type

newborn adoption

Font styles to use
Sans Serif

Colors

Designer to choose colors to be used in the design.

Requirements
Should not have
• bold or distracting colors or patterns

```html
<!DOCTYPE html>
<html lang="en">
<head>
<meta charset="utf-8">
<title>Adoption Mindset – Course Slide Set</title>
<link rel="stylesheet" href="https://fonts.googleapis.com/css2?family=Nunito:wght@400;600;700;800;900&display=swap">
<style>
  :root{
    --bg-top:#e6d3ee;
    --bg-bottom:#f1e9f4;
    --slide-faded:#eee3f2;
    --slide-white:#ffffff;
    --ink:#111111;
    --ink-soft:#3a3340;
    --muted:#8f8597;
    --accent:#a77bcf;
    --accent-soft:#e2cdef;
    --card-lilac:#efe2f3;
    --card-mauve:#e4d3ec;
    --card-pink:#ebcbe8;
    --photo-a:#b7adb9;
    --photo-b:#d9d2db;
  }
  *{box-sizing:border-box;margin:0;padding:0}
  html,body{width:1200px;height:875px;overflow:hidden}
  body{
    font-family:"Nunito",sans-serif;
    background:linear-gradient(160deg,var(--bg-top) 0%,var(--bg-bottom) 70%,#f6f1f7 100%);
    position:relative;
  }
  .deck{position:absolute;inset:0}

  /* faded overview slides */
  .thumb{
    position:absolute;background:var(--slide-faded);overflow:hidden;
    opacity:.72;color:var(--muted);
  }
  .thumb .num{position:absolute;top:5px;right:9px;font-size:6px;font-weight:700}
  .thumb h3{position:absolute;font-size:11.5px;font-weight:800;color:#8a7f91;line-height:1.15}
  .thumb h3 em{font-style:normal;color:var(--accent)}
  .thumb p{position:absolute;font-size:4.3px;line-height:1.6;color:#9c93a3}
  .photo{position:absolute;background:linear-gradient(140deg,var(--photo-b),var(--photo-a))}
  .photo.round{border-radius:40px}
  .photo.circle{border-radius:50%}
  .arc{position:absolute;border:10px solid #c4a3de;border-radius:50%}
  .heart{position:absolute}
  .stat{position:absolute;bottom:14px;width:38px;height:24px;background:#f4ecf6;border-radius:3px;text-align:center;font-size:9px;font-weight:800;color:#c9b2d9;padding-top:3px}
  .thanks-card{position:absolute;left:51px;top:33px;width:155px;height:78px;background:#a49ba7;border-radius:4px;text-align:center;color:#fff}
  .thanks-card strong{display:block;font-size:12px;margin-top:20px}
  .thanks-card span{display:block;font-size:3.5px;margin-top:4px}

  /* featured slide */
  .feature{
    position:absolute;left:67px;top:265px;width:637px;height:358px;
    background:var(--slide-white);overflow:hidden;
    box-shadow:0 14px 30px rgba(90,60,110,.22);
  }
  .feature .wash{position:absolute;inset:0}
  .feature .page{position:absolute;left:601px;top:12px;font-size:15px;font-weight:700;color:var(--accent)}
  .feature h1{position:absolute;left:192px;top:55px;font-size:28px;font-weight:900;color:var(--ink);letter-spacing:-.2px}
  .step{
    position:absolute;border-radius:4px;
    box-shadow:0 3px 8px rgba(110,80,130,.18);
    border:1.5px solid #fff;
    font-size:9px;line-height:14.5px;color:var(--ink-soft);
  }
  .step b{font-weight:800;color:var(--ink)}
  .step.lilac{background:var(--card-lilac)}
  .step.mauve{background:var(--card-mauve)}
  .step.pink{background:var(--card-pink)}
  .badge{position:absolute;width:48px;height:44px}
  .flow{position:absolute;inset:0}
</style>
</head>
<body>
<main class="deck">

  <!-- row 1 -->
  <section class="thumb" style="left:355px;top:43px;width:237px;height:144px">
    <span class="num">2</span>
    <div class="photo" role="img" aria-label="Photo of a sleeping newborn beside a soft toy" style="left:4px;top:17px;width:80px;height:90px;opacity:.6"></div>
    <h3 style="left:112px;top:30px">Introduction</h3>
    <p style="left:112px;top:48px;width:110px">A gentle start to your adoption journey and what this course will cover for you.</p>
    <div class="arc" style="left:196px;top:104px;width:70px;height:70px"></div>
  </section>

  <section class="thumb" style="left:609px;top:43px;width:256px;height:144px">
    <span class="num">3</span>
    <svg class="heart" style="left:11px;top:6px" width="18" height="18" viewBox="0 0 24 24"><path d="M12 21s-8-5.3-8-11a4.5 4.5 0 0 1 8-2.8A4.5 4.5 0 0 1 20 10c0 5.7-8 11-8 11z" fill="#c4a3de"/></svg>
    <h3 style="left:21px;top:21px">Define A Secure<br>Attachment Style</h3>
    <p style="left:21px;top:52px;width:165px">Secure attachment grows from warmth, trust and steady care in the first months.</p>
    <div class="photo" role="img" aria-label="Photo of a newborn sleeping with a headband" style="left:192px;top:21px;width:64px;height:110px"></div>
  </section>

  <section class="thumb" style="left:882px;top:43px;width:257px;height:144px">
    <span class="num">4</span>
    <h3 style="left:15px;top:47px">Information</h3>
    <p style="left:15px;top:64px;width:100px">Key facts every adoptive family should know before bringing a newborn home.</p>
    <div class="photo round" role="img" aria-label="Photo of a baby wrapped in a towel" style="left:131px;top:40px;width:47px;height:94px"></div>
    <div class="photo round" role="img" aria-label="Photo of a baby sitting on a blanket" style="left:184px;top:22px;width:60px;height:100px"></div>
    <div class="arc" style="left:-30px;top:106px;width:80px;height:80px;border-width:40px"></div>
  </section>

  <!-- row 2 -->
  <section class="thumb" style="left:355px;top:205px;width:237px;height:144px">
    <span class="num">6</span>
    <h3 style="left:2px;top:29px">What to Say When<br>Requesting Therapy</h3>
    <div class="photo" role="img" aria-label="Photo of a baby with flowers" style="left:172px;top:20px;width:65px;height:60px"></div>
  </section>

  <section class="thumb" style="left:609px;top:205px;width:256px;height:144px">
    <span class="num">7</span>
    <h3 style="left:21px;top:29px">When Therapy Is<br>Not Feasible</h3>
    <p style="left:95px;top:60px;width:42px">Simple steps you can take at home when sessions are out of reach.</p>
    <div class="photo" role="img" aria-label="Photo of an adult hand holding a baby's hand" style="left:144px;top:29px;width:88px;height:86px"></div>
  </section>

  <section class="thumb" style="left:882px;top:205px;width:257px;height:144px">
    <span class="num">8</span>
    <h3 style="left:17px;top:19px">You Decide</h3>
    <p style="left:17px;top:36px;width:140px">Choose the path that fits your family, your values and your timeline.</p>
    <div class="photo round" role="img" aria-label="Photo of a baby under a blanket" style="left:108px;top:75px;width:135px;height:46px"></div>
    <div class="arc" style="left:225px;top:96px;width:34px;height:34px;border-width:6px"></div>
  </section>

  <!-- row 3 -->
  <section class="thumb" style="left:609px;top:366px;width:256px;height:144px">
    <span class="num">11</span>
    <p style="left:122px;top:45px;width:118px">Reflect on what a right feels like and how it shapes your choices.</p>
    <div class="arc" style="left:55px;top:95px;width:98px;height:98px"></div>
    <svg class="heart" style="left:213px;top:102px" width="30" height="30" viewBox="0 0 24 24"><path d="M12 21s-8-5.3-8-11a4.5 4.5 0 0 1 8-2.8A4.5 4.5 0 0 1 20 10c0 5.7-8 11-8 11z" fill="none" stroke="#c4a3de" stroke-width="1"/></svg>
  </section>

  <section class="thumb" style="left:882px;top:366px;width:257px;height:144px">
    <span class="num">12</span>
    <h3 style="left:17px;top:23px">Money as a<br>“<em>Right.</em>”</h3>
    <div class="photo" role="img" aria-label="Photo of a baby's feet on soft fabric" style="left:137px;top:0;width:120px;height:50px;opacity:.6"></div>
    <div class="photo" role="img" aria-label="Photo of a sleeping newborn" style="left:0;top:80px;width:130px;height:64px"></div>
    <p style="left:143px;top:66px;width:100px">Plan costs early and keep records.</p>
    <p style="left:143px;top:90px;width:100px">Plan costs early and keep records.</p>
    <p style="left:143px;top:114px;width:100px">Plan costs early and keep records.</p>
  </section>

  <!-- row 4 -->
  <section class="thumb" style="left:609px;top:527px;width:256px;height:144px">
    <span class="num">15</span>
    <div class="photo circle" role="img" aria-label="Photo of a newborn" style="left:25px;top:38px;width:104px;height:104px"></div>
    <h3 style="left:122px;top:20px">Tell Me</h3>
    <p style="left:142px;top:40px;width:95px">Share your story with us.</p>
    <p style="left:142px;top:71px;width:95px">Share your story with us.</p>
    <p style="left:142px;top:102px;width:95px">Share your story with us.</p>
  </section>

  <section class="thumb" style="left:882px;top:527px;width:257px;height:144px">
    <span class="num">16</span>
    <div class="photo circle" role="img" aria-label="Portrait photo of a baby" style="left:20px;top:14px;width:33px;height:33px"></div>
    <div class="photo circle" role="img" aria-label="Portrait photo of a baby" style="left:20px;top:54px;width:33px;height:33px"></div>
    <div class="photo circle" role="img" aria-label="Portrait photo of a baby" style="left:20px;top:96px;width:33px;height:33px"></div>
    <p style="left:63px;top:23px;width:70px"><b>Nora Ellis</b><br>Notes on the first days at home.</p>
    <p style="left:60px;top:59px;width:70px"><b>Ruth Palmer</b><br>Notes on the first days at home.</p>
    <p style="left:60px;top:100px;width:70px"><b>Owen Tate</b><br>Notes on the first days at home.</p>
    <h3 style="left:152px;top:29px">The Babies</h3>
    <p style="left:165px;top:50px;width:80px"><b>4 Days Baby</b></p>
    <p style="left:165px;top:76px;width:80px"><b>8 Days Baby</b></p>
    <p style="left:165px;top:102px;width:80px"><b>12 Days Baby</b></p>
  </section>

  <!-- row 5 -->
  <section class="thumb" style="left:335px;top:687px;width:257px;height:144px">
    <span class="num">18</span>
    <div class="photo" role="img" aria-label="Photo of a baby's hand" style="left:0;top:0;width:80px;height:144px;opacity:.5"></div>
    <h3 style="left:94px;top:20px">Here’s How:</h3>
    <p style="left:94px;top:38px;width:140px">Follow these steps one week at a time to build confidence.</p>
    <div class="stat" style="left:94px">12+</div>
    <div class="stat" style="left:140px">320</div>
    <div class="stat" style="left:186px">210</div>
  </section>

  <section class="thumb" style="left:609px;top:687px;width:256px;height:144px">
    <div class="photo" role="img" aria-label="Photo of a parent holding a newborn's feet" style="left:110px;top:0;width:146px;height:144px;opacity:.7"></div>
    <h3 style="left:19px;top:42px">Case Study</h3>
    <p style="left:19px;top:60px;width:140px">A real family shares how they prepared for their first week together.</p>
  </section>

  <section class="thumb" style="left:882px;top:687px;width:257px;height:144px">
    <span class="num">20</span>
    <div class="photo" role="img" aria-label="Photo of a sleeping baby on a blanket" style="left:0;top:0;width:257px;height:144px;opacity:.55"></div>
    <div class="thanks-card">
      <strong>Thank You</strong>
      <span>Subtitle Goes Here</span>
      <span style="margin-top:12px">Clara Hunt &nbsp; April 2024</span>
    </div>
  </section>

  <!-- featured slide -->
  <section class="feature">
    <svg class="wash" viewBox="0 0 637 358" preserveAspectRatio="none" aria-hidden="true">
      <polygon points="637,35 637,358 170,358" fill="#f6f2f8"/>
    </svg>
    <svg class="heart" style="left:44px;top:9px" width="40" height="52" viewBox="0 0 40 52" aria-hidden="true">
      <path d="M15 52s-14-9-14-19a7.5 7.5 0 0 1 14-4 7.5 7.5 0 0 1 14 4c0 10-14 19-14 19z" fill="#e4d3ec"/>
      <path d="M32 22s-7-4.5-7-9.5a3.8 3.8 0 0 1 7-2 3.8 3.8 0 0 1 7 2c0 5-7 9.5-7 9.5z" fill="#e4d3ec"/>
    </svg>
    <span class="page">6</span>
    <h1>Adoption Mindset</h1>

    <svg class="flow" viewBox="0 0 637 358" aria-hidden="true">
      <g fill="none" stroke="#9b6cc7" stroke-width="1.6">
        <path d="M75 184 V265 Q75 285 95 285 H145"/>
        <path d="M228 207 Q232 181 258 181 H302"/>
        <path d="M409 232 Q409 266 440 266 H467"/>
      </g>
      <g fill="#9b6cc7">
        <path d="M140 281 L148 285 L140 289z"/>
        <path d="M297 177 L305 181 L297 185z"/>
        <path d="M462 262 L470 266 L462 270z"/>
      </g>
    </svg>

    <div class="step lilac" style="left:54px;top:112px;width:128px;height:70px;padding:23px 0 0 23px">Understand Adoption<br>Mindset</div>
    <div class="step mauve" style="left:149px;top:207px;width:129px;height:93px;padding:22px 0 0 23px">Identify Your Adoption<br>Mindset:<br><b>Right v Privilege</b></div>
    <div class="step pink" style="left:310px;top:138px;width:128px;height:93px;padding:22px 0 0 23px">Adjust Your Adoption<br>Mindset:<br><b>Right to Privilege</b></div>
    <div class="step pink" style="left:473px;top:188px;width:128px;height:124px;padding:22px 0 0 23px">Utilize Your Adoption<br>Mindset to get chosen<br>sooner :<br><b>Privilege Mindset =<br>Get chosen by a birth<br>mom sooner</b></div>

    <!-- heart badges -->
    <svg class="badge" style="left:35px;top:106px" viewBox="0 0 48 44" aria-hidden="true">
      <path d="M24 43S2 30 2 15A11 11 0 0 1 24 9a11 11 0 0 1 22 6c0 15-22 28-22 28z" fill="#e4d3ec" stroke="#fff" stroke-width="2"/>
      <g fill="none" stroke="#333" stroke-width="1.1"><path d="M24 33V22M18 20l6 4 6-4M20 33h8M17 17a3 3 0 0 1 5-1M31 17a3 3 0 0 0-5-1"/><circle cx="24" cy="16" r="3"/></g>
    </svg>
    <svg class="badge" style="left:130px;top:202px" viewBox="0 0 48 44" aria-hidden="true">
      <path d="M24 43S2 30 2 15A11 11 0 0 1 24 9a11 11 0 0 1 22 6c0 15-22 28-22 28z" fill="#e4d3ec" stroke="#fff" stroke-width="2"/>
      <g fill="none" stroke="#333" stroke-width="1.2"><circle cx="20" cy="19" r="6"/><circle cx="20" cy="19" r="3"/><path d="M24.5 23.5l8 8"/></g>
    </svg>
    <svg class="badge" style="left:291px;top:133px" viewBox="0 0 48 44" aria-hidden="true">
      <path d="M24 43S2 30 2 15A11 11 0 0 1 24 9a11 11 0 0 1 22 6c0 15-22 28-22 28z" fill="#e4d3ec" stroke="#fff" stroke-width="2"/>
      <g fill="none" stroke="#333" stroke-width="1.1"><rect x="12" y="12" width="24" height="18"/><circle cx="24" cy="21" r="4"/><circle cx="16" cy="21" r="1.5"/><circle cx="32" cy="21" r="1.5"/></g>
    </svg>
    <svg class="badge" style="left:454px;top:183px" viewBox="0 0 48 44" aria-hidden="true">
      <path d="M24 43S2 30 2 15A11 11 0 0 1 24 9a11 11 0 0 1 22 6c0 15-22 28-22 28z" fill="#e4d3ec" stroke="#fff" stroke-width="2"/>
      <g fill="none" stroke="#333" stroke-width="1.1"><path d="M13 32l4-8h7l5-3a2 2 0 0 1 2 3l-6 5h-6"/><circle cx="28" cy="13" r="2"/><path d="M25 20a3 3 0 0 1 6 0"/></g>
    </svg>
  </section>

</main>
</body>
</html>
```